A website for a Maltese Law Firm

Our law firm needs a website to further its business. The site should have a simple yet effective design. We would need the following sections: About us, Practice Areas, About Malta, Contact. These should be further split as follows:

About us: Our firm, Our values, What others say, Offices

Practice Areas: Crimimal, Citizenship & Residence, Harbour Passage Scheme, Criminal Defence, Civil Litigation, Arbitration and ADR, Commercial and Corporate, Media Law.

About Malta: just one section.

Contact: Just one section

We would also need a news feed at the front of the site to include latest news regarding our cases.

At the bottom we need a section for our Terms and a Privacy Statement.

Our logo is being attached.

Target Market(s)

All clients looking for legal assistance in Malta

Industry/Entity Type

Legal

Coding

Coded - Design and coding required

Number of Pages Required

1 page

Requirements
Must have
• It must be simple yet striking.

```html
<!DOCTYPE html>
<html lang="en">
<head>
<meta charset="utf-8">
<title>Calleja &amp; Zarbino Advocates</title>
<link rel="stylesheet" href="https://fonts.googleapis.com/css2?family=Libre+Baskerville:wght@400;700&family=Mulish:wght@400;600;800&display=swap">
<style>
:root{
  --ink:#1f1f1f;
  --text:#3a3a3a;
  --muted:#8a8a8a;
  --light:#f6f6f6;
  --line:#d8d8d8;
  --dark:#2b2b2b;
  --footer:#231f20;
  --white:#fff;
  --field:#efefef;
}
*{box-sizing:border-box;margin:0;padding:0}
html,body{width:1200px;height:2757px;overflow:hidden;background:var(--white)}
body{position:relative;font-family:"Mulish",Arial,sans-serif;color:var(--text)}
.abs{position:absolute}
.section-title{position:absolute;left:0;width:1200px;text-align:center;font-family:"Libre Baskerville",Georgia,serif;font-weight:700;font-size:24px;letter-spacing:1px;color:var(--ink)}
.section-sub{position:absolute;left:350px;width:500px;text-align:center;font-size:9.5px;line-height:15px;color:var(--muted)}

/* nav */
.nav{top:0;left:0;width:1200px;height:64px}
.nav a{position:absolute;top:24px;font-family:"Libre Baskerville",Georgia,serif;font-size:11px;color:var(--ink);text-decoration:none;white-space:nowrap}
.brand{position:absolute;left:498px;top:12px;width:204px;text-align:center;border-top:1px solid var(--ink);border-bottom:1px solid var(--ink);padding:4px 0 2px}
.brand-name{font-family:"Libre Baskerville",Georgia,serif;font-size:16px;letter-spacing:1px;color:var(--ink)}
.brand-sub{font-family:"Libre Baskerville",Georgia,serif;font-size:7px;letter-spacing:3px;color:var(--ink);margin-top:1px}

/* hero */
.hero{top:64px;left:0;width:1200px;height:272px;background:linear-gradient(180deg,#4f82b8 0%,#8db3d8 35%,#c9b894 55%,#a88e66 80%,#3e5e7a 100%)}
.hero-title{position:absolute;left:0;top:106px;width:1200px;text-align:center;color:var(--white);font-weight:800;font-size:62px;letter-spacing:-1px}

/* about */
.about-col{position:absolute;top:432px;width:170px}
.about-col h3{font-family:"Libre Baskerville",Georgia,serif;font-weight:400;font-size:14px;color:var(--ink);white-space:nowrap}
.about-col .rule{width:40px;height:1px;background:var(--line);margin:14px 0 12px}
.about-col p{font-size:9.5px;line-height:15px;color:var(--muted)}

/* testimonial */
.quote-band{top:588px;left:0;width:1200px;height:165px;background:var(--light)}
.avatar{position:absolute;left:574px;top:12px;width:52px;height:52px;border-radius:50%;background:linear-gradient(135deg,#8a9bb0,#5a6b80)}
.quote-name{position:absolute;top:72px;width:1200px;text-align:center;font-size:11px;color:var(--ink)}
.quote-text{position:absolute;left:355px;top:92px;width:490px;text-align:center;font-size:9.5px;line-height:16px;font-style:italic;color:var(--text)}
.dots{position:absolute;left:588px;top:148px;display:flex;gap:4px}
.dots span{width:4px;height:4px;border-radius:50%;background:#bbb}
.dots span.on{background:#444}

/* offices */
.office{top:871px;height:331px}
.office-a{left:0;width:600px;background:linear-gradient(180deg,#e9edf0 0%,#cfd6da 45%,#6f777c 80%,#b8bfc3 100%)}
.office-b{left:600px;width:600px;background:linear-gradient(180deg,#f4f5f2 0%,#e3e6e0 50%,#9aa29a 80%,#d9ddd6 100%)}
.arrow{position:absolute;top:1009px;width:54px;height:54px;background:rgba(40,40,40,.75)}
.arrow svg{display:block}

/* practice */
.practice-menu{top:1296px;left:244px;width:285px}
.practice-item{height:37.5px;border-bottom:1px solid #e2e2e2;background:#f1f1f1;font-size:13px;color:#666;padding-left:37px;line-height:37px;position:relative}
.practice-item::before{content:"";position:absolute;left:18px;top:15px;width:5px;height:5px;border-right:1.5px solid currentColor;border-top:1.5px solid currentColor;transform:rotate(45deg)}
.practice-item.active{background:var(--dark);color:var(--white)}
.practice-panel{top:1296px;left:529px;width:427px;height:299px;border:1px solid #cfcfcf;background:var(--light);padding:22px 28px}
.practice-panel h4{font-size:14px;font-weight:600;color:var(--ink);letter-spacing:.5px;margin-bottom:10px}
.practice-panel p{font-size:9.5px;line-height:14.5px;color:var(--muted);margin-bottom:10px}

/* malta */
.malta-text{top:1641px;left:0;width:590px;height:311px;background:var(--dark);padding:0 0 0 244px}
.malta-text h2{font-family:"Libre Baskerville",Georgia,serif;font-size:22px;color:var(--white);margin:30px 0 14px}
.malta-text p{font-size:9.5px;line-height:15px;color:#ddd;width:320px;margin-bottom:14px}
.malta-img{top:1641px;left:590px;width:610px;height:311px;background:linear-gradient(180deg,#3d5fa8 0%,#5b7cc0 45%,#c5a878 62%,#8e7450 80%,#4a5a6a 100%)}

/* news */
.news-band{top:1952px;left:0;width:1200px;height:406px;background:#f8f8f8}
.news-card{position:absolute;overflow:hidden}
.news-card span{position:absolute;left:16px;bottom:10px;right:10px;color:var(--white);font-size:14.5px;line-height:18px}

/* contact */
.field{position:absolute;left:244px;width:285px;background:var(--field);font-size:9.5px;color:#888;padding:8px 14px}
.submit{position:absolute;left:244px;top:2625px;width:101px;height:35px;background:var(--field);font-size:10px;color:#555;text-align:center;line-height:35px}
.divider{position:absolute;left:612px;top:2449px;width:1px;height:211px;background:var(--line)}
.address{position:absolute;left:634px;top:2450px;font-size:11px;line-height:17px;color:#666;font-style:normal}
.address .gap{margin-top:4px}

/* footer */
.footer{top:2704px;left:0;width:1200px;height:53px;background:var(--footer);color:var(--white);font-size:10px;font-weight:600}
.footer .l{position:absolute;left:244px;top:21px}
.footer .r{position:absolute;right:244px;top:21px}
</style>
</head>
<body>

<header class="abs nav">
  <a style="left:314px">About us</a>
  <a style="left:380px">Practice Areas</a>
  <div class="brand">
    <div class="brand-name">CALLEJA &amp; ZARBINO</div>
    <div class="brand-sub">ADVOCATES</div>
  </div>
  <a style="left:752px">About Malta</a>
  <a style="left:835px">Contact us</a>
</header>

<section class="abs hero" role="img" aria-label="Photo of the Valletta harbour skyline with a domed basilica and bell tower under a blue sky">
  <h1 class="hero-title">legal aid in Malta</h1>
</section>

<h2 class="section-title" style="top:376px">ABOUT US</h2>
<div class="about-col" style="left:244px"><h3>On the other han we</h3><div class="rule"></div><p>At vero eos et accusamus et iusto odio dignissimos ducimus qui blanditiis praesentium voluptatum deleniti atque corrupti quos dolores et quas molestias excepturi sint</p></div>
<div class="about-col" style="left:426px"><h3>Finibus Bonorum et</h3><div class="rule"></div><p>Sed ut perspiciatis unde omnis iste natus error sit voluptatem accusantium doloremque laudantium, totam rem aperiam, eaque ipsa quae ab illo inventore veritatis et quasi</p></div>
<div class="about-col" style="left:610px"><h3>Lorem ipsum dolor sit</h3><div class="rule"></div><p>Nemo enim ipsam voluptatem quia voluptas sit aspernatur aut odit aut fugit, sed quia consequuntur magni dolores eos qui ratione voluptatem sequi nesciunt.</p></div>
<div class="about-col" style="left:792px"><h3>Sed ut perspiciatis unde</h3><div class="rule"></div><p>Ut enim ad minima veniam, quis nostrum exercitationem ullam corporis suscipit laboriosam, nisi ut aliquid ex ea commodi consequatur?</p></div>

<section class="abs quote-band">
  <div class="avatar" role="img" aria-label="Client portrait"></div>
  <div class="quote-name">Elena Marsh</div>
  <p class="quote-text">"On the other hand, we denounce with righteous indignation and dislike men who are so beguiled and demoralized by the charms of pleasure of the moment, so blinded by desire, that they cannot foresee the pain and trouble that are bound to ensue; and equal blame belongs to those who fail in their duty."</p>
  <div class="dots"><span></span><span class="on"></span><span></span><span></span></div>
</section>

<h2 class="section-title" style="top:786px">OFFICES</h2>
<p class="section-sub" style="top:822px">On the other hand, we denounce with righteous indignation and dislike men who are so beguiled and demoralized by the charms of pleasure of the moment, so blinded by desire, that they cannot foresee the</p>
<div class="abs office office-a" role="img" aria-label="Photo of an open-plan office floor with rows of desks and chairs"></div>
<div class="abs office office-b" role="img" aria-label="Photo of a bright white office with desks and a green accent wall"></div>
<div class="arrow" style="left:520px"><svg width="54" height="54" viewBox="0 0 54 54"><path d="M31 16 L21 27 L31 38" fill="none" stroke="#fff" stroke-width="3"/></svg></div>
<div class="arrow" style="left:626px"><svg width="54" height="54" viewBox="0 0 54 54"><path d="M23 16 L33 27 L23 38" fill="none" stroke="#fff" stroke-width="3"/></svg></div>

<h2 class="section-title" style="top:1240px">PRACTISE AREAS</h2>
<nav class="abs practice-menu">
  <div class="practice-item active">Crimimal</div>
  <div class="practice-item">Citizenship &amp; Residence</div>
  <div class="practice-item">Harbour Passage Scheme</div>
  <div class="practice-item">Criminal Defence</div>
  <div class="practice-item">Civil Litigation</div>
  <div class="practice-item">Arbitration and ADR</div>
  <div class="practice-item">Commercial and Corporate</div>
  <div class="practice-item">Media Law</div>
</nav>
<article class="abs practice-panel">
  <h4>CRIMINAL AS VETRO IPSUM</h4>
  <p>Sed ut perspiciatis unde omnis iste natus error sit voluptatem accusantium doloremque laudantium, totam rem aperiam, eaque ipsa quae ab illo inventore veritatis et quasi architecto beatae vitae dicta sunt explicabo.</p>
  <p>Nemo enim ipsam voluptatem quia voluptas sit aspernatur aut odit aut fugit, sed quia consequuntur magni dolores eos qui ratione voluptatem sequi nesciunt.</p>
  <p>Neque porro quisquam est, qui dolorem ipsum quia dolor sit amet, consectetur, adipisci velit, sed quia non numquam eius modi tempora incidunt ut labore et dolore magnam aliquam quaerat voluptatem.</p>
  <p>Ut enim ad minima veniam, quis nostrum exercitationem ullam corporis suscipit laboriosam, nisi ut aliquid ex ea commodi consequatur? Quis autem vel eum iure reprehenderit qui in ea voluptate velit esse quam nihil molestiae consequatur, vel illum qui dolorem eum fugiat quo voluptas nulla pariatur?</p>
</article>

<section class="abs malta-text">
  <h2>About Malta</h2>
  <p>At vero eos et accusamus et iusto odio dignissimos ducimus qui blanditiis praesentium voluptatum deleniti atque corrupti quos dolores et quas molestias excepturi sint occaecati cupiditate non provident.</p>
  <p>Similique sunt in culpa qui officia deserunt mollitia animi, id est laborum et dolorum fuga.Et harum quidem rerum facilis est et expedita distinctio.<br>Nam libero tempore, cum soluta nobis est eligendi optio cumque nihil impedit quo minus id quod maxime placeat facere possimus, omnis voluptas assumenda est, omnis dolor repellendus.</p>
  <p>Temporibus autem quibusdam et aut officiis debitis aut rerum necessitatibus saepe eveniet ut et voluptates repudiandae sint et molestiae non recusandae.</p>
</section>
<div class="abs malta-img" role="img" aria-label="Photo of Valletta's limestone skyline with a basilica dome and spire against a deep blue sky"></div>

<section class="abs news-band"></section>
<h2 class="section-title" style="top:1987px">OUR NEWS</h2>
<p class="section-sub" style="top:2021px">On the other hand, we denounce with righteous indignation and dislike men who are so beguiled and demoralized by the charms of pleasure of the moment, so blinded by desire, that they cannot foresee the</p>
<div class="news-card" style="left:244px;top:2064px;width:346px;height:112px;background:linear-gradient(135deg,#4b5d7a,#2c3446 60%,#6b7b93)" role="img" aria-label="News photo of officers escorting a detained man"><span>Lorem ipsum situation</span></div>
<div class="news-card" style="left:244px;top:2195px;width:164px;height:119px;background:linear-gradient(180deg,#6a3f22,#2a1a10)" role="img" aria-label="News photo of a lawyer speaking in a wood-panelled courtroom"><span>At vero eos et accusamus et iusto</span></div>
<div class="news-card" style="left:426px;top:2195px;width:164px;height:119px;background:linear-gradient(180deg,#7a4a2c,#3a2418)" role="img" aria-label="News photo of a woman seated in a courtroom"><span>At vero eos et accusamus et iusto</span></div>
<div class="news-card" style="left:610px;top:2064px;width:346px;height:250px;background:linear-gradient(160deg,#6b3c22,#3a1e10 60%,#1e0f08)" role="img" aria-label="News photo of brass scales of justice and a judge's gavel on law books"><span>At vero eos et accusamus et iusto odio</span></div>

<h2 class="section-title" style="top:2394px;left:244px;width:auto;text-align:left">CONTACT US</h2>
<div class="field" style="top:2455px;height:28px">Name</div>
<div class="field" style="top:2490px;height:26px">Email</div>
<div class="field" style="top:2524px;height:86px">Message</div>
<div class="submit">Submit</div>
<div class="divider"></div>
<address class="address">
  Merchants 42 Str.<br>VLT 1170, Valletta<br>Malta
  <div class="gap">+356-2100-4471 (landline)</div>
  <div class="gap">+356-7900-2385 (mobile phone)</div>
  <div class="gap">+356-2100-4472 (fax)</div>
</address>

<footer class="abs footer">
  <span class="l">Terms and a Privacy Statement</span>
  <span class="r">Copyright 2016</span>
</footer>

</body>
</html>
```